Property Management Services Proposal - Powerpoint template

We need a proposal template for our multifamily property management services. We have a simple/generic handout that we use (uploaded here) but we need something for an actual proposal/client presentation standpoint. A powerpoint file that includes company/team overview, some placeholders for the specific client we would be proposing too, etc. Website is www.quillonpropertyservices.com

Target Market(s)

Residential/Multifamily Property Owners and Investors

Industry/Entity Type

Real Estate

Font styles to use
Sans Serif

Colors
0355a3
f78f20
9d9d9d
ffffff

Requirements
Must have
• Logo, color scheme (orange, navy, gray) - clean look but not overly simple. Placeholders for specific projects, case studies, timelines, photos, graphs, etc.

```html
<!DOCTYPE html>
<html lang="en">
<head>
<meta charset="utf-8">
<title>Property Management Proposal – Slide Layouts</title>
<link href="https://fonts.googleapis.com/css2?family=Lato:wght@400;700&display=swap" rel="stylesheet">
<style>
  :root {
    --panel-grey: #5e5e5e;
    --heading-navy: #0355a3;
    --body-grey: #555555;
    --light-grey: #cfcfcf;
    --mid-grey: #9d9d9d;
    --accent-orange: #f47d20;
    --paper: #ffffff;
    --photo-cool: #b9d3e6;
  }
  * { margin: 0; padding: 0; box-sizing: border-box; }
  html, body { width: 900px; height: 1200px; overflow: hidden; background: var(--paper); }
  body { position: relative; font-family: 'Lato', sans-serif; color: var(--body-grey); }

  .slide {
    position: absolute; left: 66px; width: 768px; height: 432px;
    background: var(--paper);
    box-shadow: 1px 2px 4px rgba(0,0,0,0.35);
    overflow: hidden;
  }
  .slide--intro { top: 29px; }
  .slide--contact { top: 490px; }

  .panel-grey { position: absolute; top: 0; height: 100%; background: var(--panel-grey); }
  .photo { position: absolute; box-shadow: 0 3px 8px rgba(0,0,0,0.55); }

  /* Slide 4 */
  .slide--intro .panel-grey { left: 0; width: 302px; }
  .slide--intro .photo {
    left: 16px; top: 16px; width: 270px; height: 400px;
    background: linear-gradient(180deg, #d7e3ea 0%, #8a6c5e 35%, #5b3c33 60%, #9b8f92 100%);
  }
  .intro-body { position: absolute; left: 330px; top: 0; width: 394px; }
  .slide-title {
    font-weight: 700; color: var(--heading-navy);
    font-size: 29px; text-align: center; margin-top: 29px; letter-spacing: -0.2px;
  }
  .slide-lead {
    color: var(--accent-orange); font-size: 15px; line-height: 19px;
    text-align: center; margin-top: 6px;
  }
  .bullet-list { list-style: none; margin-top: 56px; }
  .bullet-list li {
    position: relative; padding-left: 18px; font-size: 10.4px; line-height: 13.5px;
    text-align: justify; margin-bottom: 9.5px;
  }
  .bullet-list li::before {
    content: ""; position: absolute; left: 3px; top: 3px; width: 6px; height: 6px;
    background: var(--accent-orange);
  }
  .intro-note { font-size: 10.4px; line-height: 13.5px; text-align: justify; margin-top: 16px; }

  .brand-mark {
    position: absolute; font-family: 'Lato', sans-serif; font-weight: 400;
    color: var(--accent-orange); font-size: 20px; letter-spacing: 0.5px;
  }
  .slide--intro .brand-mark { left: 320px; top: 394px; }
  .page-number { position: absolute; font-size: 9px; }
  .slide--intro .page-number { left: 719px; top: 406px; color: var(--body-grey); }

  /* Slide 7 */
  .slide--contact .panel-grey { left: 257px; width: 511px; }
  .contact-side { position: absolute; left: 23px; top: 0; width: 212px; }
  .contact-title { font-weight: 700; color: var(--heading-navy); font-size: 26px; margin-top: 30px; }
  .contact-lead { color: var(--accent-orange); font-size: 12.2px; line-height: 15.3px; margin-top: 6px; }
  .tile-row { position: absolute; left: 52px; top: 211px; display: flex; gap: 11px; }
  .tile { width: 45px; height: 45px; display: flex; align-items: center; justify-content: center; }
  .tile--navy { background: var(--heading-navy); }
  .tile--light { background: var(--light-grey); }
  .tile--orange { background: var(--accent-orange); }
  .contact-tagline {
    position: absolute; left: 30px; width: 208px; top: 279px;
    text-align: center; font-weight: 700; color: var(--heading-navy);
    font-size: 18px; line-height: 23px;
  }
  .slide--contact .brand-mark { left: 108px; top: 394px; }
  .slide--contact .photo {
    left: 272px; top: 13px; width: 223px; height: 400px;
    background: linear-gradient(160deg, var(--photo-cool) 0%, #e8eef4 45%, #a9c2da 100%);
  }
  .contact-copy { position: absolute; left: 525px; top: 54px; width: 196px; color: #ffffff; }
  .contact-copy p { font-size: 10.5px; line-height: 13.4px; margin-bottom: 9px; }
  .slide--contact .page-number { left: 719px; top: 408px; color: #ffffff; font-weight: 700; }
</style>
</head>
<body>

<section class="slide slide--intro">
  <div class="panel-grey"></div>
  <div class="photo" role="img" aria-label="Photo of a cobbled street lined with lit brick buildings at dusk"></div>
  <div class="intro-body">
    <h1 class="slide-title">Lorem ipsum dolor sit amet</h1>
    <p class="slide-lead">Lorem ipsum dolor sit amet, consectetuer adipiscing elit.<br>Aenean commodo ligula eget dolor.</p>
    <ul class="bullet-list">
      <li>Lorem ipsum dolor sit amet, consectetuer adipiscing elit. Aenean commodo ligula eget dolor. Aenean massa.</li>
      <li>Cum sociis natoque penatibus et magnis dis parturient montes, nascetur ridiculus mus. Donec quam felis, ultricies nec, pellentesque eu, pretium quis, sem. Nulla consequat massa quis enim.</li>
      <li>Donec pede justo, fringilla vel, aliquet nec, vulputate eget, arcu.</li>
      <li>In enim justo, rhoncus ut, imperdiet a, venenatis vitae, justo. Nullam dictum felis eu pede mollis pretium. Integer tincidunt. Cras dapibus.</li>
    </ul>
    <p class="intro-note">Aliquam lorem ante, dapibus in, viverra quis, feugiat a, tellus. Phasellus viverra nulla ut metus varius laoreet. Quisque rutrum. Aenean imperdiet. Etiam ultricies nisi vel augue. Curabitur ullamcorper ultricies nisi.</p>
  </div>
  <div class="brand-mark">QPS</div>
  <div class="page-number">4</div>
</section>

<section class="slide slide--contact">
  <div class="contact-side">
    <h2 class="contact-title">Lorem ipsum</h2>
    <p class="contact-lead">Lorem ipsum dolor sit amet, consectetuer adipiscing elit. Aenean commodo ligula eget dolor. Aenean massa. Cum sociis natoque penatibus et magnis dis parturient montes, nascetur ridiculus mus.</p>
  </div>
  <div class="tile-row">
    <div class="tile tile--navy"></div>
    <div class="tile tile--light">
      <svg width="22" height="26" viewBox="0 0 22 26" aria-hidden="true">
        <circle cx="12" cy="6" r="4" fill="#ffffff"/>
        <path d="M5 26 V15 Q5 11 9 11 H15 Q19 11 19 15 V26 Z" fill="#ffffff"/>
        <path d="M4 3 Q1 6 4 10" stroke="#ffffff" stroke-width="2" fill="none"/>
      </svg>
    </div>
    <div class="tile tile--orange"></div>
  </div>
  <p class="contact-tagline">Lorem ipsum<br>dolor sit amet,<br>consectetuer.</p>
  <div class="brand-mark">QPS</div>

  <div class="panel-grey"></div>
  <div class="photo" role="img" aria-label="Photo of a smiling customer service agent wearing a headset"></div>
  <div class="contact-copy">
    <p>Lorem ipsum dolor sit amet, consectetuer adipiscing elit. Aenean commodo ligula eget dolor. Aenean massa. Cum sociis natoque penatibus et magnis dis parturient montes, nascetur ridiculus mus. Donec quam felis, ultricies nec, pellentesque eu, pretium quis, sem. Nulla consequat massa quis enim. Donec pede justo, fringilla vel, aliquet nec, vulputate eget, arcu.</p>
    <p>In enim justo, rhoncus ut, imperdiet a, venenatis vitae, justo. Nullam dictum felis eu pede mollis pretium. Integer tincidunt. Cras dapibus. Vivamus elementum semper nisi. Aenean vulputate eleifend tellus. Aenean leo ligula, porttitor eu, consequat vitae, eleifend ac, enim.</p>
    <p>Aliquam lorem ante, dapibus in, viverra quis, feugiat a, tellus. Phasellus viverra nulla ut metus varius laoreet. Quisque rutrum. Aenean imperdiet. Etiam ultricies nisi vel augue. Curabitur ullamcorper ultricies nisi.</p>
  </div>
  <div class="page-number">7</div>
</section>

</body>
</html>
```